GLP letterhead

We need a letterhead design for our new company based in Los Angeles called "Gold Ladder Pictures". We develop film and television projects. We work with investors, financiers, film production companies, film distribution and sales companies as well as studios. We would like to incorporate our logo (see attached) but make the letterhead simple and elegant. We need to include: logo, company address, phone number and company website.
Updates

Hello designers, Thanks for your submissions. For our letterhead, we are looking for something more simple and elegant. No heavy bars or lines. Make it feel light and clean. Not a lot of ink on the page. Use the logo and contact info but think "clean", "streamlined" and mostly white paper. Looking forward to seeing more... thanks! Gold Ladder Pictures team

Target Market(s)

Studio executives, talent agents and agencies, financiers, investors.

Industry/Entity Type

It Company

Requirements
Must have
• Gold Ladder Pictures logo (see attached). Logo may be cropped and altered appropriately for elegant letterhead design.
• Please include:
• COMPANY ADDRESS:
• TQV Media Campus
• 2750 Halvering Avenue
• Norwick Center, 4th Floor
• Farrowdale Cove, CA 90999
• COMPANY WEBSITE:
• www.goldladderpicturesgroup.example
• COMPANY PHONE NUMBER:
• 555-014-2236

```html
<!DOCTYPE html>
<html lang="en">
<head>
<meta charset="utf-8">
<title>Gold Ladder Pictures — Letterhead</title>
<link rel="stylesheet" href="https://fonts.googleapis.com/css2?family=Open+Sans:wght@400;600&display=swap">
<style>
  :root {
    --backdrop: #e6e4e1;
    --paper: #ffffff;
    --ink: #4a4a4a;
    --ink-soft: #6b6b6b;
    --brand: #1b86c4;
    --brand-dark: #0d2a3a;
    --rule: #bdbdbd;
  }
  * { margin: 0; padding: 0; box-sizing: border-box; }
  html, body {
    width: 950px; height: 1200px; overflow: hidden;
    background: var(--backdrop);
    font-family: "Open Sans", Arial, sans-serif;
  }
  .sheet {
    position: absolute; left: 50px; top: 50px;
    width: 850px; height: 1098px;
    background: var(--paper);
    box-shadow: 0 1px 4px rgba(0,0,0,.12);
  }
  .brand {
    position: absolute; left: 40px; top: 22px; width: 164px;
    display: flex; flex-direction: column; align-items: center;
  }
  .brand-dot {
    width: 98px; height: 98px; border-radius: 50%;
    background: var(--brand-dark);
  }
  .brand-name {
    margin-top: 8px;
    font-size: 13px; font-weight: 600; letter-spacing: .06em;
    color: var(--brand); text-transform: uppercase; white-space: nowrap;
  }
  .divider {
    position: absolute; left: 267px; top: 74px;
    width: 1px; height: 84px;
    background: linear-gradient(to bottom, transparent, var(--rule) 30%, var(--rule) 70%, transparent);
  }
  .contact {
    position: absolute; left: 296px; top: 73px;
    color: var(--ink); list-style: none;
  }
  .contact-line {
    display: flex; align-items: center; gap: 5px;
    font-size: 14px; line-height: 26px;
  }
  .contact-line svg { width: 13px; height: 13px; flex: none; }
  .address {
    margin-top: 2px; font-size: 12.5px; line-height: 16px; color: var(--ink);
  }
</style>
</head>
<body>
  <main class="sheet">
    <header>
      <div class="brand">
        <div class="brand-dot" aria-hidden="true"></div>
        <div class="brand-name">Gold Ladder Pictures</div>
      </div>
      <div class="divider" aria-hidden="true"></div>
      <ul class="contact">
        <li class="contact-line">
          <svg viewBox="0 0 16 16" aria-hidden="true"><circle cx="8" cy="8" r="7.2" fill="none" stroke="#555" stroke-width="1"/><path d="M5.4 4.2c-.9.6-1 1.8-.3 3.3.8 1.8 2.3 3.5 3.8 4.2 1 .5 1.8.3 2.3-.4l-1.5-1.5-1 .5C7.9 9.8 6.8 8.6 6.5 7.7l.8-.8z" fill="#555"/></svg>
          <span>555-014-2236</span>
        </li>
        <li class="contact-line">
          <svg viewBox="0 0 16 16" aria-hidden="true"><g fill="none" stroke="#666" stroke-width=".9"><circle cx="8" cy="8" r="6.5"/><ellipse cx="8" cy="8" rx="3" ry="6.5"/><path d="M1.5 8h13M2.5 4.8h11M2.5 11.2h11"/></g></svg>
          <span>www.goldladderpicturesgroup.example</span>
        </li>
        <li class="address">
          TQV Media Campus 2750 Halvering Avenue Norwick Center,<br>
          4th Floor Farrowdale Cove, CA 90999
        </li>
      </ul>
    </header>
  </main>
</body>
</html>
```